Bramwell HVAC Service LLC Business Card

We just got a design created by one of your designers for a logo and now would like help with a business card design. The information to be included on the card is as follows:
Bramwell HVAC Service LLC (I will attach logo design)
P.O. Box 482
Dunmore, CO 80634
(970) 347-6159
Lonnie Tadwick
I might include an e-mail address, but I'm not sure yet.
Target Market(s)
Customers needing service or repairs done on their heating and air conditioning systems.
Industry/Entity Type
Business
Contact Information for Business Card
P.O. Box 482
Dunmore, CO 80634
(970) 347-6159
Lonnie Tadwick

```html
<!DOCTYPE html>
<html lang="en">
<head>
<meta charset="utf-8">
<title>Bramwell HVAC Service LLC – Business Card</title>
<link rel="stylesheet" href="https://fonts.googleapis.com/css2?family=Montserrat:wght@500;700;800&display=swap">
<style>
  :root {
    --navy: #1f3370;
    --red: #e1222b;
    --card: #f2f2f0;
    --ink: #1d2a55;
    --stage: #d9dadc;
  }
  * { margin: 0; padding: 0; box-sizing: border-box; }
  html, body { width: 1200px; height: 516px; overflow: hidden; }
  body {
    position: relative;
    background: var(--stage);
    font-family: "Montserrat", Arial, sans-serif;
    color: var(--ink);
  }
  .card {
    position: absolute;
    background: var(--card);
    overflow: hidden;
    box-shadow: 0 4px 12px rgba(0,0,0,0.18);
  }
  .card--front { left: 140px; top: 134px; width: 438px; height: 246px; }
  .card--back  { left: 606px; top: 139px; width: 454px; height: 240px; border-top: 2px solid var(--navy); }

  .brand { position: absolute; display: flex; align-items: center; gap: 10px; }
  .brand__mark { width: 34px; height: 34px; background: var(--navy); flex: none; }
  .brand__name {
    font-weight: 800; color: var(--navy); line-height: 1.05;
    text-transform: uppercase; letter-spacing: 0.5px;
  }
  .card--front .brand { left: 26px; top: 30px; }
  .card--front .brand__name { font-size: 17px; }
  .card--back .brand { left: 72px; top: 102px; }
  .card--back .brand__mark { width: 44px; height: 44px; }
  .card--back .brand__name { font-size: 21px; }

  .holder {
    position: absolute; left: 26px; top: 120px; width: 392px;
    font-size: 15px; font-weight: 700; color: var(--navy);
    letter-spacing: 0.6px; text-transform: uppercase;
    padding-bottom: 3px; border-bottom: 1px solid var(--navy);
  }
  .contact { position: absolute; left: 26px; top: 152px; list-style: none; }
  .contact li {
    display: flex; align-items: center; gap: 4px;
    font-size: 12.5px; font-weight: 500; line-height: 14.5px; color: var(--ink);
  }
  .contact svg { width: 10px; height: 10px; fill: var(--ink); flex: none; }
  .contact .contact__address { margin-top: 9px; font-size: 13px; }
  .contact .contact__address svg { width: 11px; height: 12px; }

  .band { position: absolute; left: 0; bottom: 0; width: 438px; height: 24px; }
</style>
</head>
<body>
  <section class="card card--front" aria-label="Business card front">
    <div class="brand">
      <span class="brand__mark"></span>
      <span class="brand__name">Bramwell HVAC<br>Service LLC</span>
    </div>

    <h1 class="holder">Lonnie Tadwick</h1>

    <ul class="contact">
      <li><svg viewBox="0 0 10 10"><rect x="0" y="0" width="10" height="10" rx="1.5"/><path d="M3 2.2l1 1.6-.7.7c.4.9 1.1 1.6 2 2l.7-.7 1.6 1-.5 1.2C4.6 8 2 5.4 1.9 2.7z" fill="#f2f2f0"/></svg>(970) 347-6159</li>
      <li><svg viewBox="0 0 10 10"><rect x="0" y="2" width="10" height="6.5" rx="0.8"/><path d="M0.5 2.6L5 6l4.5-3.4" stroke="#f2f2f0" stroke-width="0.9" fill="none"/></svg>ltadwick@bramwellhvacservice.com</li>
      <li><svg viewBox="0 0 10 10"><circle cx="5" cy="5" r="4.3" fill="none" stroke="#1d2a55" stroke-width="1"/><ellipse cx="5" cy="5" rx="1.9" ry="4.3" fill="none" stroke="#1d2a55" stroke-width="0.8"/><path d="M0.8 5h8.4" stroke="#1d2a55" stroke-width="0.8"/></svg>www.bramwellhvacservice.com</li>
      <li class="contact__address"><svg viewBox="0 0 11 12"><path d="M5.5 0C2.8 0 1 2 1 4.4 1 7.5 5.5 12 5.5 12S10 7.5 10 4.4C10 2 8.2 0 5.5 0z"/><circle cx="5.5" cy="4.3" r="1.7" fill="#f2f2f0"/></svg>P.O. Box 482 Dunmore, CO 80634</li>
    </ul>

    <svg class="band" viewBox="0 0 438 24" preserveAspectRatio="none" aria-hidden="true">
      <path d="M0 4H278c8 0 10 1.5 12 4l3 4H0z" fill="var(--navy)"/>
      <path d="M0 13.5H286c6 0 9-2 11-6l2-3.5c2-3 4-4 8-4H438V24H0z" fill="var(--red)"/>
    </svg>
  </section>

  <section class="card card--back" aria-label="Business card back">
    <div class="brand">
      <span class="brand__mark"></span>
      <span class="brand__name">Bramwell HVAC<br>Service LLC</span>
    </div>
  </section>
</body>
</html>
```